hobby beef jerky maker looking to break into the commercial market

We need product labels designed for each flavour of jerky we make. Currently have 3 flavours that we are ready to share with the world. We need in your face designs to help us stand out from an already crowded market.
The product name is Rowdy Beef Jerky.
The flavours we offer have been named Porch Party, Tangy Glow and Fiery Bite.
The Rowdy Beef Jerky Title should remain the same across the three labels but the design for each flavour can change as you see fit.
Label needs to fit within 110mm x 110mm to suit our current packaging

Industry/Entity Type

Food Production

Logo Text

Morvathen Clover

Colors

Designer to choose colors to be used in the design.

Requirements
Must have
• "Rowdy Beef Jerky" font and colour must remain the same across the 3 designs
Nice to have
• The labels will be used on the clear side of the packaging with a small space towards the bottom being left visible so the product inside can be seen

```html
<!DOCTYPE html>
<html lang="en">
<head>
<meta charset="utf-8">
<title>Rowdy Beef Jerky – Porch Party Label</title>
<link rel="stylesheet" href="https://fonts.googleapis.com/css2?family=Fredoka:wght@600;700&family=Cormorant+Garamond:wght@600&family=Open+Sans:wght@500&display=swap">
<style>
  :root {
    --page: #ffffff;
    --ink: #111111;
    --bronze-dark: #3e2414;
    --bronze-mid: #7a4e28;
    --bronze-light: #bd9158;
    --bronze-top: #a57c3c;
    --maroon: #4a0808;
    --frame-grey: #6b6b6b;
    --frame-light: #9a9a9a;
    --sage: #c0c09c;
    --brand-blue: #1e80f2;
    --cream: #ffffff;
    --cocoa: #3d2314;
    --badge-red: #5a0f0f;
  }
  * { box-sizing: border-box; margin: 0; padding: 0; }
  html, body {
    width: 1200px; height: 1000px; overflow: hidden;
    background: var(--page);
  }
  .canvas { position: relative; width: 1200px; height: 1000px; }

  .size-note {
    position: absolute; top: 18px; left: 0; width: 1164px;
    text-align: center;
    font-family: "Cormorant Garamond", serif; font-weight: 600;
    font-size: 64px; color: var(--ink); letter-spacing: 1px;
  }

  .label {
    position: absolute; left: 184px; top: 108px;
    width: 868px; height: 789px; overflow: hidden;
    background: linear-gradient(90deg, var(--bronze-dark) 0%, var(--bronze-mid) 16%, var(--bronze-light) 50%, var(--bronze-mid) 84%, var(--bronze-dark) 100%);
  }
  .label__top {
    position: absolute; left: 0; top: 0; width: 100%; height: 110px;
    background: linear-gradient(90deg, var(--bronze-dark) 0%, var(--bronze-mid) 18%, var(--bronze-top) 50%, var(--bronze-mid) 82%, var(--bronze-dark) 100%);
  }
  .label__foot {
    position: absolute; left: 0; bottom: 0; width: 100%; height: 48px;
    background: linear-gradient(90deg, #2e1a0e 0%, #6a4423 30%, #7d5630 50%, #6a4423 70%, #2e1a0e 100%);
  }

  .title-panel {
    position: absolute; left: 4px; top: 88px;
    width: 860px; height: 366px;
    background: var(--maroon);
    border: 12px solid var(--frame-grey);
    border-radius: 62px 62px 0 0;
  }

  .quality-badge {
    position: absolute; left: 710px; top: 12px;
    width: 144px; height: 144px; border-radius: 50%;
    background: var(--badge-red);
    border: 4px solid #f3e6da;
    box-shadow: 0 0 0 3px var(--badge-red);
  }

  .brand-plate {
    position: absolute; left: 174px; top: 114px;
    width: 514px; height: 126px;
    background: var(--sage);
    border: 9px solid #555555;
    border-radius: 26px;
    display: flex; align-items: center; justify-content: center;
  }
  .brand-name {
    font-family: "Fredoka", sans-serif; font-weight: 700;
    font-size: 104px; line-height: 1; letter-spacing: 3px;
    color: var(--brand-blue);
    -webkit-text-stroke: 3px var(--cream);
    paint-order: stroke fill;
  }

  .product-name {
    position: absolute; left: 0; top: 256px; width: 868px;
    text-align: center;
    font-family: "Fredoka", sans-serif; font-weight: 700;
    font-size: 118px; line-height: 1; letter-spacing: 6px;
    color: var(--cream);
  }

  .flavour-pill {
    position: absolute; left: 71px; top: 402px;
    width: 720px; height: 82px;
    background: var(--cream);
    border: 6px solid var(--cocoa);
    border-radius: 26px;
    display: flex; align-items: baseline; justify-content: center; gap: 18px;
    padding-top: 6px;
    font-family: "Fredoka", sans-serif; font-weight: 700;
    color: var(--cocoa);
  }
  .flavour-pill__name { font-size: 58px; letter-spacing: 2px; line-height: 64px; }
  .flavour-pill__word { font-size: 40px; letter-spacing: 1px; }

  .premium-artwork {
    position: absolute; left: 62px; top: 522px;
    width: 354px; height: 214px;
    background: linear-gradient(180deg, var(--maroon), #5a1a12);
    border-radius: 60px 90px 20px 30px;
  }

  .net-weight {
    position: absolute; left: 661px; top: 644px;
    width: 140px; height: 118px;
    background: #3a1e12;
    border: 8px solid var(--frame-light);
    border-radius: 40px 40px 6px 6px;
    box-shadow: 0 3px 8px rgba(0,0,0,.5);
    display: flex; align-items: center; justify-content: center;
    font-family: "Open Sans", sans-serif; font-weight: 500;
    font-size: 40px; color: var(--cream);
  }
</style>
</head>
<body>
<div class="canvas">
  <p class="size-note">110 mm x 110 mm</p>

  <section class="label">
    <div class="label__top"></div>
    <div class="label__foot"></div>

    <div class="title-panel"></div>
    <div class="quality-badge" role="img" aria-label="Round premium quality beef badge"></div>

    <div class="brand-plate"><span class="brand-name">ROWDY</span></div>
    <h1 class="product-name">BEEF JERKY</h1>

    <div class="flavour-pill">
      <span class="flavour-pill__name">PORCH PARTY</span>
      <span class="flavour-pill__word">FLAVOUR</span>
    </div>

    <div class="premium-artwork" role="img" aria-label="Cow silhouette carrying a premium quality laurel emblem"></div>

    <div class="net-weight">00 g</div>
  </section>
</div>
</body>
</html>
```